Business Card Design Project

We need a business card for a new technology services company. We develop software and implement software packages for our business customers and although we will begin with just one or two service offerings, our service offerings will expand over time. Our name comes from the an author, Corvale, and his "idea" was that opportunity should be based on ability and achievement, not on social status.

We would like to see a design that is standard in its size and shape, but stands apart in its dramatic color contrasts. The card should not use too many colors - the colors used in the background should highlight the brilliant blues of the logo (see attachment) to dramatic effect. The background should not be white.

If necessary, you can change the color of the words "Corvale", but not the word "Idea".

Card size should be U.S. standard 2 inches by 3.5 inches and provide for 1/8 inch bleed area on each side.

We need a design for both sides of the business card, one side communicating the company logo and contact information, the other side being purely graphical, incorporating the logo but no other information.

Contact Information Required:
Mark Linden
MarkLinden@corvalelabs.com
555-304-7812

Target Market(s)

Business executives

Industry/Entity Type

Software

Requirements
Must have
• It must have the full company logo on one side, and at least the graphic element of the logo on the other. Either that or the full logo on both.
Nice to have
• It would be nice to have a design that could work without needing two different textures. For example, it would be nice if the entire card could be shiny, not just parts of the card.

It would also be nice if texture is something we could add later.
Should not have
• The card should not use the color green.

```html
<!DOCTYPE html>
<html lang="en">
<head>
<meta charset="utf-8">
<title>Corvale Labs – Business Card</title>
<link rel="stylesheet" href="https://fonts.googleapis.com/css2?family=Open+Sans:wght@300;400;600;700&display=swap">
<style>
  :root {
    --page: #ffffff;
    --card-dark: #000000;
    --card-glow: #161616;
    --brand-blue: #0095d5;
    --frame-blue: #0a93d6;
    --text-light: #ffffff;
    --text-soft: #e6e6e6;
  }
  * { margin: 0; padding: 0; box-sizing: border-box; }
  html, body {
    width: 1200px; height: 900px; overflow: hidden;
    background: var(--page);
    font-family: "Open Sans", Arial, sans-serif;
  }
  .card {
    position: absolute; left: 156px; top: 197px;
    width: 888px; height: 508px;
    background: var(--card-dark);
    overflow: hidden;
  }
  .card-backdrop {
    position: absolute; left: 0; top: 0; width: 888px; height: 369px;
    background: radial-gradient(ellipse at 45% 45%, var(--card-glow) 0%, var(--card-dark) 75%);
  }
  .frame-lines { position: absolute; left: 0; top: 0; }
  .wordmark {
    position: absolute; left: 162px; top: 200px;
    font-size: 60px; font-weight: 600; letter-spacing: -1.5px;
    color: var(--brand-blue); line-height: 1; white-space: nowrap;
  }
  .person {
    position: absolute; right: 120px; top: 280px; text-align: center;
    color: var(--text-light);
  }
  .person-name { font-size: 26px; font-weight: 700; letter-spacing: 0.5px; line-height: 34px; }
  .person-role { font-size: 22px; font-weight: 300; color: var(--text-soft); line-height: 30px; }
  .contact-band {
    position: absolute; left: 0; top: 369px; width: 888px; height: 139px;
    background: var(--brand-blue);
  }
  .contact-item {
    position: absolute; display: flex; align-items: center;
    color: var(--text-light); font-size: 21px; font-weight: 400; white-space: nowrap;
  }
  .contact-icon {
    width: 23px; height: 23px; border-radius: 5px;
    background: var(--text-light); color: var(--brand-blue);
    font-size: 16px; font-weight: 400;
    display: flex; align-items: center; justify-content: center;
    margin-right: 19px;
  }
  .contact-item.right .contact-icon { margin-right: 11px; }
  .email   { left: 47px;  top: 19px; }
  .website { left: 47px;  top: 61px; }
  .phone   { left: 531px; top: 19px; }
  .address { left: 531px; top: 61px; }
</style>
</head>
<body>
  <div class="card">
    <div class="card-backdrop" role="img" aria-label="Dark background with a scattered pattern of soft grey ovals"></div>
    <svg class="frame-lines" width="888" height="369" viewBox="0 0 888 369" aria-hidden="true">
      <polyline points="130,101 130,304 330,304" fill="none" stroke="var(--frame-blue)" stroke-width="4"/>
      <polyline points="571,61 771,61 771,263" fill="none" stroke="var(--frame-blue)" stroke-width="4"/>
    </svg>
    <div class="wordmark">Corvale Labs</div>
    <div class="person">
      <div class="person-name">MARK LINDEN</div>
      <div class="person-role">Business Manager</div>
    </div>
    <div class="contact-band">
      <div class="contact-item email"><span class="contact-icon">E</span>MarkLinden@corvalelabs.com</div>
      <div class="contact-item website"><span class="contact-icon">W</span>www.corvalelabs.com</div>
      <div class="contact-item right phone"><span class="contact-icon">T</span>555-304-7812</div>
      <div class="contact-item right address"><span class="contact-icon">A</span>213 Street Name , Abcdefghij</div>
    </div>
  </div>
</body>
</html>
```